PowerPoint Template - Multiple Slide Backgrounds

Looking for a professional PowerPoint template for a technology company. You will see with the logo there's sort of a theme with gears and a lightbulb of sorts. Keeping with this sort of design could help with the brand.

Branding information
• Logo with transparent background included
• Primary Color (Orange) Hex #E6753D
• Secondary Color (Brown) Hex #6A4238
• Primary Font - Myriad Pro
• Secondary Font - Quiet Sans Light

Design request -
• PowerPoint (POTX) template with master slide views
• Cover Slide
• Color Pallet - 7 Color PowerPoint pallet that includes and complements primary and secondary colors
• Slide Master with Footer
• Multiple Background Types to allow for smart art overlay or bullet point text boxes
Bonus - Sample graphical elements using shapes and smart art

```html
<!DOCTYPE html>
<html lang="en">
<head>
<meta charset="utf-8">
<title>Bullet Slides</title>
<link rel="stylesheet" href="https://fonts.googleapis.com/css2?family=Source+Sans+3:wght@300;400;600;700&display=swap">
<style>
  :root {
    --orange: #e6753d;
    --brown: #6a4238;
    --body-grey: #7a7a7a;
    --rule-grey: #c9c9c9;
    --white: #ffffff;
  }
  * { margin: 0; padding: 0; box-sizing: border-box; }
  html, body { width: 1200px; height: 653px; overflow: hidden; background: var(--white); }
  .slide {
    position: relative;
    width: 1200px;
    height: 653px;
    overflow: hidden;
    background: var(--white);
    font-family: "Source Sans 3", "Myriad Pro", sans-serif;
  }
  .title-rule {
    position: absolute; left: 64px; top: 0;
    width: 1px; height: 224px; background: var(--rule-grey);
  }
  .title-accent {
    position: absolute; left: 57px; top: 66px;
    width: 9px; height: 86px; background: var(--orange); border-radius: 2px;
  }
  .title-block { position: absolute; left: 90px; top: 70px; }
  .subtitle { color: var(--orange); font-size: 28px; font-weight: 400; line-height: 1.05; }
  .title { color: var(--brown); font-size: 37px; font-weight: 700; line-height: 1.05; }
  .brand {
    position: absolute; right: 28px; top: 26px;
    display: flex; align-items: center; gap: 10px;
    color: var(--orange); font-size: 26px; font-weight: 700;
  }
  .brand-dot { width: 18px; height: 18px; border-radius: 50%; background: var(--brown); }
  .bullets { position: absolute; left: 90px; top: 184px; width: 1000px; list-style: none; }
  .bullet { margin-bottom: 48px; }
  .bullet-head { display: flex; align-items: center; gap: 14px; }
  .bullet-icon { width: 24px; height: 24px; border-radius: 50%; background: var(--orange); margin-left: 4px; }
  .bullet-title { color: var(--orange); font-size: 27px; font-weight: 700; line-height: 34px; }
  .bullet-text {
    margin-left: 46px; color: var(--body-grey);
    font-size: 16.5px; font-weight: 300; line-height: 30px;
  }
  .footer-band {
    position: absolute; left: 0; top: 608px;
    width: 1106px; height: 44px; background: var(--brown);
    border-radius: 0 22px 22px 0;
    display: flex; align-items: center; padding-left: 17px;
    color: var(--white); font-size: 18px; font-weight: 400;
  }
  .page-number {
    position: absolute; left: 1131px; top: 608px;
    width: 80px; height: 44px; background: var(--orange);
    border-radius: 18px 0 0 18px;
    display: flex; align-items: center; padding-left: 22px;
    color: var(--white); font-size: 20px; font-weight: 700;
  }
</style>
</head>
<body>
<div class="slide">
  <div class="title-rule"></div>
  <div class="title-accent"></div>
  <header class="title-block">
    <p class="subtitle">Subtitle Here</p>
    <h1 class="title">Bullet Slides</h1>
  </header>

  <div class="brand"><span class="brand-dot"></span>Cogwell</div>

  <ul class="bullets">
    <li class="bullet">
      <div class="bullet-head"><span class="bullet-icon"></span><h2 class="bullet-title">Bullet text Here</h2></div>
      <p class="bullet-text">Lorem Ipsum is simply dummy text of the printing and typesetting industry. Lorem Ipsum has been the industry's standard dummy text ever since the 1500s, when an unknown printer took a galley of type and scrambled it to make a type specimen book.</p>
    </li>
    <li class="bullet">
      <div class="bullet-head"><span class="bullet-icon"></span><h2 class="bullet-title">Bullet text Here</h2></div>
      <p class="bullet-text">Lorem Ipsum is simply dummy text of the printing and typesetting industry. Lorem Ipsum has been the industry's standard dummy text ever since the 1500s, when an unknown printer took a galley of type and scrambled it to make a type specimen book.</p>
    </li>
    <li class="bullet">
      <div class="bullet-head"><span class="bullet-icon"></span><h2 class="bullet-title">Bullet text Here</h2></div>
      <p class="bullet-text">Lorem Ipsum is simply dummy text of the printing and typesetting industry. Lorem Ipsum has been the industry's standard dummy text ever since the 1500s, when an unknown printer took a galley of type and scrambled it to make a type specimen book.</p>
    </li>
  </ul>

  <footer>
    <div class="footer-band">Copyright text here</div>
    <div class="page-number">01</div>
  </footer>
</div>
</body>
</html>
```